Postcard Design Fine Art Postcard Design

I need a postcard design that would include 2 - 3 pictures of my paintings and my web address
Updates

I do not need room on the back of the card for a stamp or address lines as I will be handing them out, not mailing them. Having the extra room may help with the layout of the pictures.

Target Market(s)

Upper, upper middle class buyers looking to acquire original art for their homes, apts, condos, offices.

Font styles to use
Sans Serif

Requirements
Must have
• Must be professional looking and include samples of my paintings.
Nice to have
• N/A

```html
<!DOCTYPE html>
<html lang="en">
<head>
<meta charset="utf-8">
<title>Mara Lindell Fine Art – Postcard</title>
<link href="https://fonts.googleapis.com/css2?family=Alegreya+Sans+SC:wght@500&family=Arimo:ital,wght@0,400;1,400&display=swap" rel="stylesheet">
<style>
  :root {
    --backdrop: #e4c99a;
    --card-cream: #efe6cf;
    --card-cream-light: #f8f2e1;
    --card-cream-edge: #e6d6b2;
    --frame-brown: #b39357;
    --ink: #1d1a16;
    --art-child: linear-gradient(135deg, #b9c3cc 0%, #c0414a 40%, #d9dde2 65%, #c6b8a4 100%);
    --art-boats: linear-gradient(180deg, #9fb1c4 0%, #7f8f9f 55%, #3a4552 100%);
    --art-barn: linear-gradient(160deg, #4e6a3a 0%, #9a8e83 40%, #b5734a 60%, #5e6e3a 100%);
    --art-abstract: linear-gradient(180deg, #d8c59c 0%, #c8a468 45%, #8b5a2b 62%, #d6c4a0 100%);
    --art-beach: linear-gradient(180deg, #2b8fd0 0%, #5fc1c9 35%, #dff2f2 55%, #3c7fd6 100%);
  }
  * { box-sizing: border-box; margin: 0; padding: 0; }
  html, body { width: 1200px; height: 500px; overflow: hidden; }
  body {
    position: relative;
    background: var(--backdrop);
    font-family: "Arimo", Arial, sans-serif;
    color: var(--ink);
  }
  .card { position: absolute; }
  .card--front {
    left: 22px; top: 33px; width: 558px; height: 435px;
    background: var(--card-cream);
    box-shadow: 0 1px 4px rgba(0,0,0,.18);
  }
  .card--back {
    left: 613px; top: 35px; width: 555px; height: 430px;
    border: 7px solid var(--frame-brown);
    background: radial-gradient(ellipse at 50% 45%, var(--card-cream-light) 55%, var(--card-cream-edge) 100%);
  }
  .studio-name {
    font-family: "Alegreya Sans SC", "Trebuchet MS", sans-serif;
    font-weight: 500;
    letter-spacing: .5px;
    color: var(--ink);
  }
  .card--front .studio-name {
    position: absolute; left: 66px; top: 55px; font-size: 25px;
  }
  .web-address { color: var(--ink); }
  .card--front .web-address {
    position: absolute; left: 0; width: 100%; top: 384px;
    text-align: center; font-size: 24px;
  }
  .painting { position: absolute; }
  .painting--child { left: 28px; top: 120px; width: 295px; height: 252px; background: var(--art-child); }
  .painting--boats { left: 365px; top: 34px; width: 158px; height: 125px; background: var(--art-boats); }
  .painting--barn { left: 365px; top: 172px; width: 158px; height: 200px; background: var(--art-barn); }
  .painting--abstract { left: 17px; top: 23px; width: 229px; height: 233px; background: var(--art-abstract); }
  .painting--beach { left: 284px; top: 180px; width: 210px; height: 158px; background: var(--art-beach); }
  .artist-quote {
    position: absolute; left: 265px; top: 25px; width: 270px;
    font-size: 14px; line-height: 19px;
  }
  .artist-quote .attribution {
    display: block; margin-top: 8px; text-align: center;
    font-style: italic;
  }
  .card--back .back-footer {
    position: absolute; left: 0; width: 100%; top: 358px; text-align: center;
  }
  .card--back .studio-name { font-size: 19px; line-height: 22px; }
  .card--back .web-address { font-size: 15px; line-height: 20px; }
</style>
</head>
<body>
  <section class="card card--front">
    <h1 class="studio-name">Mara Lindell Fine Art</h1>
    <div class="painting painting--child" role="img" aria-label="Painting of a child in a red cap crouching on a beach"></div>
    <div class="painting painting--boats" role="img" aria-label="Painting of shrimp boats docked in misty blue water"></div>
    <div class="painting painting--barn" role="img" aria-label="Painting of a rusted tin barn among green trees"></div>
    <p class="web-address">www.maralindell.com</p>
  </section>

  <section class="card card--back">
    <div class="painting painting--abstract" role="img" aria-label="Abstract palette-knife painting in ochre and umber tones"></div>
    <p class="artist-quote">
      Whenever my grandfather visited he would bring a big box of crayons and we would draw for hours. The love of color propels my art to this day and I am continually delighted by the variety of color in nature.
      <span class="attribution">Mara Lindell</span>
    </p>
    <div class="painting painting--beach" role="img" aria-label="Painting of a father and small child holding hands in ocean surf"></div>
    <div class="back-footer">
      <p class="studio-name">Mara Lindell Fine Art</p>
      <p class="web-address">www.maralindell.com</p>
    </div>
  </section>
</body>
</html>
```